Eye-Catching, Direct Marketing Residential Painting Flyer!

I am run a residential painting business and am looking for a flyer to be designed to mailout to potential customers.
I want the copy/wording to be designed similar to this flyer.

It's important that the person reading the flyer gets the benefits we're promoting which is why I want the wording/copy to be almost identical to the flyer attached.

However, the structure will be different. The flyer will be a postcard thick, 5 x11.5.
Double sided.

The name of the company is Brightwall Coaters.

I would also like the prominent colour to either be light green or orange.

Target Market(s)

Home Owners between the age of 45-80.

Industry/Entity Type

Painting And Decorating

Font styles to use
Serif

Colors
f68d4d
faa54b
f78f20
f37122
9bcb3c
abd037
cadf82

Requirements
Must have
• Excellent Eye-Catching Design
• Benefits Visibly Promoted
• Action Taking Incentive- Call Now for FREE Window Cleaning and FREE Painting Estimate
Should not have
• Crowded wording

```html
<!DOCTYPE html>
<html lang="en">
<head>
<meta charset="utf-8">
<title>Brightwall Coaters – Postcard Mailer</title>
<link href="https://fonts.googleapis.com/css2?family=Lora:ital,wght@0,400;0,600;0,700;1,400&family=Merriweather:wght@700;900&display=swap" rel="stylesheet">
<style>
:root{
  --orange:#f78f20;
  --orange-deep:#f37122;
  --orange-soft:#faa54b;
  --coral:#f68d4d;
  --green:#9bcb3c;
  --green-lime:#abd037;
  --green-pale:#cadf82;
  --ink:#3f3f3f;
  --muted:#6f6f6f;
  --paper:#ffffff;
  --page:#eeeeee;
  --head:"Merriweather",Georgia,serif;
  --body:"Lora",Georgia,serif;
}
*{margin:0;padding:0;box-sizing:border-box}
html,body{width:828px;height:1200px;overflow:hidden;background:var(--page)}
body{font-family:var(--body);color:var(--ink);position:relative}

.card-side{position:absolute;top:144px;width:396px;height:911px;background:var(--paper);box-shadow:0 2px 8px rgba(0,0,0,.18);overflow:hidden}
.card-side--front{left:12px}
.card-side--back{left:420px}
.block{position:absolute;left:0;width:100%}

/* front */
.brand{top:24px;display:flex;align-items:center;justify-content:center;gap:10px}
.brand-dot{width:30px;height:30px;border-radius:50%;background:var(--orange);flex:none}
.brand-name{font-family:var(--head);font-weight:900;font-size:20px;color:var(--green);text-transform:uppercase;letter-spacing:.3px}
.lead{top:84px;padding:0 28px;text-align:center;font-size:13px;line-height:1.45;color:var(--muted)}
.promise{top:152px;padding:0 28px;text-align:center;font-family:var(--head);font-weight:700;font-size:14px;line-height:1.45;color:var(--ink)}
.painter-photo{top:212px;height:240px;background:linear-gradient(140deg,#eef1f4,#cdd6dc 50%,#8fa0ab)}
.photo-wedge{position:absolute;top:400px;left:0}
.control-band{top:452px;height:58px;background:var(--green);color:#fff;font-family:var(--head);font-weight:900;font-size:15px;line-height:1.35;text-align:center;padding:9px 16px 0;text-transform:uppercase}
.offers{top:530px;display:flex;justify-content:center;gap:12px}
.offer{width:170px;height:100px;border:1px dashed var(--orange);text-align:center;font-size:10.5px;line-height:1.4;padding:9px 10px;color:var(--ink)}
.offer strong{color:var(--orange-deep)}
.cta{top:650px;padding:0 26px;text-align:center;color:var(--orange-deep);font-family:var(--head);font-weight:900;font-size:16px;line-height:1.4}
.phone-band{top:716px;height:50px;background:var(--green);display:flex;align-items:center;justify-content:center;gap:10px;color:#fff;font-family:var(--head);font-weight:900;font-size:20px}
.web{top:782px;text-align:center;color:var(--green);font-family:var(--head);font-weight:700;font-size:13px}
.paint-art{top:815px;height:96px;background:
  linear-gradient(90deg,var(--green) 0 25%,#f4d23a 25% 50%,var(--orange) 50% 75%,#e4412b 75%)}

/* back */
.testimonials{top:0;height:240px;background:var(--orange);padding:22px 24px 0 20px;display:flex;flex-direction:column;gap:16px}
.quote{display:flex;gap:12px;align-items:flex-start}
.quote svg{flex:none}
.quote p{font-size:11.5px;line-height:1.4;color:#fff}
.quote .who{display:block;font-style:italic;font-size:10px;opacity:.92}

.problem-row{position:absolute;left:16px;width:364px;height:200px;display:flex;gap:12px}
.problem-row--deck{top:258px}
.problem-row--garage{top:476px}
.problem-row--kitchen{top:694px}
.scene{width:128px;height:200px;border-radius:4px;flex:none}
.scene--deck{background:linear-gradient(170deg,#c9b9a2,#8a6d52 60%,#5a4432)}
.scene--garage{background:linear-gradient(170deg,#e7e4de,#b6b0a6 60%,#6f6a61)}
.scene--kitchen{background:linear-gradient(170deg,#f3ead8,#c9b48f 60%,#7a6447)}
.fix-card{flex:1;border-radius:4px;color:#fff;text-align:center;padding:16px 14px 0}
.fix-card--orange{background:var(--orange)}
.fix-card--green{background:var(--green)}
.fix-card h3{font-family:var(--head);font-size:13px;font-weight:900;margin-bottom:4px}
.fix-card p{font-size:10.5px;line-height:1.45;margin-bottom:10px}
</style>
</head>
<body>

<section class="card-side card-side--front">
  <div class="block brand"><span class="brand-dot"></span><span class="brand-name">Brightwall Coaters</span></div>
  <p class="block lead">Does your dark interior or dirty walls, fence, windows look faded, dirty, out of date, are they chipping or peeling?</p>
  <p class="block promise">We make your home look<br>CLEAN, FRESH &amp; Beautiful again!</p>
  <div class="block painter-photo" role="img" aria-label="Smiling painter in white overalls holding a paint roller"></div>
  <svg class="photo-wedge" width="396" height="52" viewBox="0 0 396 52"><polygon points="0,52 396,0 396,52" fill="#9bcb3c"/><polygon points="0,44 396,8 396,18 0,54" fill="#f78f20"/></svg>
  <div class="block control-band">Take control of how<br>your home looks!</div>
  <div class="block offers">
    <div class="offer">If you are one of the <strong>first 15 exterior projects</strong> booked with us, you will receive a complimentary <strong>window cleaning</strong>.</div>
    <div class="offer">If you are one of the <strong>first 15 interior projects</strong> booked with us, you will receive a complimentary <strong>window cleaning</strong>.</div>
  </div>
  <p class="block cta">Call Now for FREE Window Cleaning and FREE Painting Estimate</p>
  <div class="block phone-band">
    <svg width="20" height="20" viewBox="0 0 24 24"><path fill="#fff" d="M6.6 10.8a15.1 15.1 0 0 0 6.6 6.6l2.2-2.2a1 1 0 0 1 1-.25 11.4 11.4 0 0 0 3.6.57 1 1 0 0 1 1 1V20a1 1 0 0 1-1 1A17 17 0 0 1 3 4a1 1 0 0 1 1-1h3.5a1 1 0 0 1 1 1c0 1.25.2 2.45.57 3.57a1 1 0 0 1-.25 1z"/></svg>
    555-218-4490
  </div>
  <p class="block web">www.brightwallcoaters.com</p>
  <div class="block paint-art" role="img" aria-label="Paint rollers laying green, yellow, orange and red stripes of paint"></div>
</section>

<section class="card-side card-side--back">
  <div class="block testimonials">
    <div class="quote">
      <svg width="22" height="22" viewBox="0 0 22 22"><circle cx="11" cy="11" r="11" fill="#fff"/><text x="11" y="18" text-anchor="middle" font-size="18" font-weight="700" fill="#f78f20" font-family="Georgia, serif">“</text></svg>
      <p>Wonderful job, very neat and on time. Our house looks new again!<span class="who">– Helen M., Homeowner</span></p>
    </div>
    <div class="quote">
      <svg width="22" height="22" viewBox="0 0 22 22"><circle cx="11" cy="11" r="11" fill="#fff"/><text x="11" y="18" text-anchor="middle" font-size="18" font-weight="700" fill="#f78f20" font-family="Georgia, serif">“</text></svg>
      <p>They painted our fence and deck quickly and left everything spotless. Great crew, fair price.<span class="who">– Robert D., Homeowner</span></p>
    </div>
    <div class="quote">
      <svg width="22" height="22" viewBox="0 0 22 22"><circle cx="11" cy="11" r="11" fill="#fff"/><text x="11" y="18" text-anchor="middle" font-size="18" font-weight="700" fill="#f78f20" font-family="Georgia, serif">“</text></svg>
      <p>Very happy with the kitchen colours. We will call them again.<span class="who">– Linda &amp; Tom K., Homeowners</span></p>
    </div>
  </div>

  <div class="problem-row problem-row--deck">
    <div class="scene scene--deck" role="img" aria-label="Stained wooden backyard deck with patio furniture"></div>
    <div class="fix-card fix-card--orange">
      <h3>Problem</h3>
      <p>Your deck or fence is chipping or peeling, and looks old and faded.</p>
      <h3>Solution</h3>
      <p>A fresh coat of stain will protect your investment and make it look new, fresh and beautiful again!</p>
    </div>
  </div>

  <div class="problem-row problem-row--garage">
    <div class="scene scene--garage" role="img" aria-label="House front with freshly painted white garage doors"></div>
    <div class="fix-card fix-card--orange">
      <h3>Problem</h3>
      <p>Your exterior windows, doors, garage doors, stucco, siding and soffits are chipping, peeling, and look old and faded.</p>
      <h3>Solution</h3>
      <p>A fresh coat of paint will protect your investment and make it look new, fresh and beautiful again!</p>
    </div>
  </div>

  <div class="problem-row problem-row--kitchen">
    <div class="scene scene--kitchen" role="img" aria-label="Bright kitchen interior with freshly painted walls"></div>
    <div class="fix-card fix-card--green">
      <h3>Problem</h3>
      <p>The colours in your basement, kitchen, bedrooms and bathroom walls, doors and trim look out of date and faded.</p>
      <h3>Solution</h3>
      <p>A fresh coat of paint to make your rooms look clean, fresh and beautiful again!</p>
    </div>
  </div>
</section>

</body>
</html>
```